Client Handbook for Modern building company

We are seeking a cover for our client handbook for print and eBook, would like it to be modern and streamlined, this will be a first impression when starting a project for a new client. possibly containing the photo of one of our projects (attached) or something resembling a successful relationship with a client? handshake etc

Requirements
Must have
• Our logo (attached) and our tagline "creating tomorrow" , the words Client Handbook,

```html
<!DOCTYPE html>
<html lang="en">
<head>
<meta charset="utf-8">
<title>Northvale Builders – Client Handbook</title>
<link rel="stylesheet" href="https://fonts.googleapis.com/css2?family=Barlow:wght@300;600&family=Russo+One&display=swap">
<style>
  :root {
    --sky: #a0d8f4;
    --leaf: #b5d69d;
    --orange: #d9843f;
    --forest: #1f7a4f;
    --slate: #97a8b4;
    --ink: #2a2a2a;
    --paper: #ffffff;
  }
  html, body {
    margin: 0;
    padding: 0;
    overflow: hidden;
    background: var(--paper);
  }
  .cover {
    position: relative;
    width: 771px;
    height: 1200px;
    overflow: hidden;
    background: var(--paper);
    font-family: "Barlow", Arial, sans-serif;
  }
  .shapes {
    position: absolute;
    inset: 0;
  }
  .brand {
    position: absolute;
    left: 418px;
    top: 96px;
    width: 304px;
    height: 50px;
    display: flex;
    align-items: center;
    gap: 12px;
  }
  .brand-mark {
    width: 48px;
    height: 48px;
    border-radius: 50%;
    background: var(--ink);
    flex: none;
  }
  .brand-name {
    font-family: "Barlow", Arial, sans-serif;
    font-weight: 600;
    font-size: 22px;
    letter-spacing: 1px;
    color: var(--ink);
    white-space: nowrap;
  }
  .tagline {
    position: absolute;
    right: 47px;
    top: 246px;
    margin: 0;
    text-align: right;
    font-family: "Barlow", Arial, sans-serif;
    font-weight: 300;
    font-size: 60px;
    line-height: 55px;
    color: var(--orange);
  }
  .title {
    position: absolute;
    right: 49px;
    top: 1004px;
    margin: 0;
    text-align: right;
    font-family: "Russo One", Arial, sans-serif;
    font-weight: 400;
    font-size: 45px;
    line-height: 45px;
    letter-spacing: -1px;
    color: var(--slate);
    text-transform: uppercase;
  }
  .dots {
    position: absolute;
    left: 656px;
    top: 1122px;
    display: flex;
    gap: 8px;
  }
  .dots span {
    width: 10px;
    height: 10px;
    border-radius: 50%;
    background: var(--slate);
  }
</style>
</head>
<body>
<main class="cover">
  <svg class="shapes" width="771" height="1200" viewBox="0 0 771 1200">
    <defs>
      <linearGradient id="family-tones" x1="0" y1="0" x2="1" y2="0.7">
        <stop offset="0" stop-color="#5f7d3a"/>
        <stop offset="0.25" stop-color="#8a7048"/>
        <stop offset="0.45" stop-color="#b9805e"/>
        <stop offset="0.62" stop-color="#a8d24f"/>
        <stop offset="0.8" stop-color="#7f9a4a"/>
        <stop offset="1" stop-color="#4f6a2e"/>
      </linearGradient>
      <linearGradient id="house-tones" x1="0.2" y1="0" x2="0.35" y2="1">
        <stop offset="0" stop-color="#7ea5e8"/>
        <stop offset="0.22" stop-color="#a6c2ee"/>
        <stop offset="0.32" stop-color="#54575c"/>
        <stop offset="0.55" stop-color="#6e7074"/>
        <stop offset="0.72" stop-color="#b9b9b6"/>
        <stop offset="0.85" stop-color="#8d9092"/>
        <stop offset="1" stop-color="#c8c8c4"/>
      </linearGradient>
    </defs>

    <polygon class="band-top" points="0,0 457,0 427,80 0,80" fill="var(--sky)"/>

    <polygon class="photo-family" role="img" aria-label="Photo of a smiling mother holding her toddler outdoors in a green park"
             points="0,160 397,160 302,415 0,415" fill="url(#family-tones)"/>

    <rect class="photo-house" role="img" aria-label="Photo of a completed two-storey townhouse with dark and white cladding, garage and fenced courtyard"
          x="0" y="415" width="771" height="523" fill="url(#house-tones)"/>

    <polygon class="overlay-orange" points="0,415 302,415 168,712 0,422" fill="var(--orange)" opacity="0.92"/>
    <polygon class="overlay-green" points="0,422 297,938 0,938" fill="var(--forest)" opacity="0.94"/>

    <polygon class="band-sky" points="0,938 105,938 8,1196 0,1196" fill="var(--sky)"/>
    <polygon class="band-leaf" points="105,938 297,938 8,1196" fill="var(--leaf)"/>
  </svg>

  <div class="brand">
    <span class="brand-mark"></span>
    <span class="brand-name">NORTHVALE BUILDERS</span>
  </div>

  <h2 class="tagline">Creating<br>Tomorrow</h2>

  <h1 class="title">Client<br>Handbook</h1>

  <div class="dots"><span></span><span></span><span></span><span></span></div>
</main>
</body>
</html>
```